Physician and Alternative Investments Investor needs a business card design.

I am making a career change from a plastic surgeon to a career as an investor. I am primarily involved with Angel Investing. I really want a fairly simple design overall and don't need to list angel investing unless it can be done very subtly, perhaps via an image rather than verbiage. A design without any mention of angel investing is completely acceptable. My credentials are "MD, MBA." I will also want to place my email address and mobile phone number and have provided below.

Target Market(s)

business contacts (physicians and non-physicians in the business world)

Industry/Entity Type

Business

Requirements
Must have
• Colin Marsh
• MD, MBA
• drcolinmarsh@quillmail.test
• cell 555.018.2364
Should not have
• Clutter.

```html
<!DOCTYPE html>
<html lang="en">
<head>
<meta charset="utf-8">
<title>Colin Marsh — Business Cards</title>
<link rel="stylesheet" href="https://fonts.googleapis.com/css2?family=Questrial&display=swap">
<style>
  :root {
    --page-bg: #eceae6;
    --card-bg: #ffffff;
    --navy: #1d3f7c;
    --ink: #2a2a2a;
    --muted: #6b6b6b;
    --rule: #a9a9a9;
    --pattern-light: #f3f6fa;
    --pattern-tone: #e4eaf2;
    --shadow: rgba(0, 0, 0, 0.14);
  }
  * { box-sizing: border-box; margin: 0; padding: 0; }
  html, body {
    width: 1200px; height: 900px; overflow: hidden;
    background: var(--page-bg);
    font-family: "Questrial", "Century Gothic", sans-serif;
  }
  .stage { position: relative; width: 1200px; height: 900px; }

  .card {
    position: absolute;
    width: 540px; height: 310px;
    background: var(--card-bg);
    box-shadow: 0 10px 24px var(--shadow);
    overflow: hidden;
  }
  .card--front { left: 60px; top: 130px; }
  .card--back { left: 600px; top: 460px; }

  /* soft tonal field where the faint monogram pattern belongs */
  .pattern-field {
    position: absolute; inset: 0;
    background: linear-gradient(160deg, var(--pattern-tone) 0%, var(--pattern-light) 55%, var(--card-bg) 100%);
  }

  .identity { display: flex; flex-direction: column; align-items: center; }
  .identity__name {
    color: var(--navy);
    font-size: 38px;
    font-weight: 400;
    letter-spacing: 0.5px;
    line-height: 1.05;
    white-space: nowrap;
  }
  .identity__rule {
    width: 100%;
    border-top: 1px solid var(--rule);
    margin-top: 8px;
    display: flex; justify-content: center;
  }
  .identity__credentials {
    position: relative; top: -9px;
    background: var(--card-bg);
    padding: 0 8px;
    color: var(--muted);
    font-size: 14px;
    letter-spacing: 1.5px;
  }

  .card--front .identity { position: absolute; right: 40px; top: 180px; }

  .card--back .identity { position: absolute; left: 150px; top: 200px; }
  .card--back .identity__name { font-size: 36px; }
  .mark {
    position: absolute; left: 176px; top: 92px;
    color: var(--navy);
    font-size: 80px;
    line-height: 1;
  }

  .contact {
    position: absolute; right: 26px; top: 28px;
    list-style: none;
    font-size: 13px;
    color: var(--ink);
  }
  .contact li { display: flex; align-items: center; gap: 8px; margin-bottom: 5px; }
  .contact svg { width: 14px; height: 14px; flex: none; }
</style>
</head>
<body>
<main class="stage">

  <section class="card card--front" aria-label="Card front">
    <div class="pattern-field" role="img" aria-label="Faint repeated monogram pattern in pale blue"></div>
    <div class="identity">
      <h1 class="identity__name">Colin Marsh</h1>
      <div class="identity__rule"><span class="identity__credentials">MD, MBA</span></div>
    </div>
  </section>

  <section class="card card--back" aria-label="Card back">
    <ul class="contact">
      <li>
        <svg viewBox="0 0 14 14" aria-hidden="true">
          <rect width="14" height="14" rx="2" fill="var(--navy)"/>
          <path d="M3 4.5c0-1 .8-1.5 4-1.5s4 .5 4 1.5v1H9v-1H5v1H3z M4 7h6l1 4H3z" fill="#fff"/>
        </svg>
        <span>555.018.2364</span>
      </li>
      <li>
        <svg viewBox="0 0 14 14" aria-hidden="true">
          <rect width="14" height="14" rx="2" fill="var(--navy)"/>
          <rect x="3" y="4" width="8" height="6" fill="none" stroke="#fff" stroke-width="1"/>
          <path d="M3 4l4 3.2L11 4" fill="none" stroke="#fff" stroke-width="1"/>
        </svg>
        <span>drcolinmarsh@quillmail.test</span>
      </li>
    </ul>
    <div class="mark" aria-label="Colin Marsh initials">CM</div>
    <div class="identity">
      <h2 class="identity__name">Colin Marsh</h2>
      <div class="identity__rule"><span class="identity__credentials">MD, MBA</span></div>
    </div>
  </section>

</main>
</body>
</html>
```